Aerial Photography Brochure

I need a brochure designed around my company logo and around aerial photography. We use drones to capture jobsite progression, real estate, and commercial jobs. I like designs with the color blue and that show people we are professional and sophisticated.

Industry/Entity Type

Real Estate

Font styles to use
Serif

Colors
3276b5
0293ce
33a6d7
86cae7
85abd2
3176b5
0355a3

Requirements
Must have
• Must have My logo and our info to contact and to view our website.
Nice to have
• Not crazy artistic i just want something that looks very professional and gets people to look at my website
Should not have
• Hours of operation

```html
<!DOCTYPE html>
<html lang="en">
<head>
<meta charset="utf-8">
<title>Highpoint Aerial Imaging – Aerial Photography Brochure</title>
<link rel="stylesheet" href="https://fonts.googleapis.com/css2?family=Roboto+Condensed:wght@300;400;700&family=Source+Sans+3:wght@400;600;700&display=swap">
<style>
  :root{
    --blue-deep:#0355a3;
    --blue-main:#0293ce;
    --blue-mid:#3176b5;
    --blue-soft:#33a6d7;
    --blue-pale:#86cae7;
    --charcoal:#2b2b2d;
    --ink:#222;
    --paper:#ffffff;
    --stage:#e4e5e7;
  }
  *{box-sizing:border-box;margin:0;padding:0}
  html,body{width:1200px;height:1200px;overflow:hidden;background:var(--stage)}
  body{position:relative;font-family:"Source Sans 3",Arial,sans-serif;color:var(--ink)}
  .spread{position:absolute;left:228px;width:878px;height:626px;transform:scale(.8576);transform-origin:0 0;background:var(--paper);box-shadow:0 4px 14px rgba(0,0,0,.28);overflow:hidden}
  .spread--cover{top:34px}
  .spread--inside{top:617px}
  .spread svg.art{position:absolute;left:0;top:0;width:878px;height:626px}
  .fold{position:absolute;left:430px;top:0;width:20px;height:626px;background:linear-gradient(90deg,rgba(0,0,0,0),rgba(0,0,0,.08) 50%,rgba(0,0,0,0))}
  .ph{position:absolute}

  .drone-photo{left:24px;top:62px;width:392px;height:242px;border-radius:6px;
    background:
      radial-gradient(ellipse 42% 30% at 50% 52%,rgba(30,31,34,.85) 0%,rgba(60,61,64,.55) 55%,rgba(60,61,64,0) 100%),
      linear-gradient(180deg,#f4f4f4 0%,#e4e4e5 60%,#d6d6d8 100%);
    box-shadow:inset 0 0 0 1px rgba(0,0,0,.04)}

  .brand{position:absolute;font-family:"Source Sans 3",Arial,sans-serif;font-weight:600;letter-spacing:.06em;text-transform:uppercase;line-height:1.12;display:flex;align-items:center;gap:8px}
  .brand__dot{width:12px;height:12px;border-radius:50%;background:currentColor;flex:none}
  .brand--back{left:236px;top:512px;color:#fff;font-size:17px}
  .brand--front{left:580px;top:76px;color:var(--blue-deep);font-size:25px}
  .brand--inside{left:36px;top:196px;color:var(--blue-deep);font-size:21px}

  .contact{position:absolute;left:40px;top:468px;color:#fff;font-size:10.5px;font-weight:700;line-height:14px}
  .contact h4{font-size:11px;margin-bottom:7px}
  .contact li{list-style:none;display:flex;gap:5px;align-items:flex-start}
  .contact svg{width:8px;height:8px;margin-top:3px;flex:none}
  .contact .label{margin:4px 0 0 13px}

  .cover-title{position:absolute;left:500px;width:340px;text-align:center;font-family:"Roboto Condensed",Arial,sans-serif}
  .cover-title .light{display:block;font-weight:400;font-size:50px;color:var(--charcoal);line-height:1;margin-top:452px}
  .cover-title .bold{display:block;font-weight:700;font-size:52px;color:var(--blue-main);line-height:1;letter-spacing:.01em}
  .web-pill{position:absolute;left:515px;top:561px;width:305px;height:34px;border-radius:17px;background:var(--charcoal);border:2px solid #fff;box-shadow:0 2px 4px rgba(0,0,0,.4);color:#fff;font-size:13px;letter-spacing:.28em;text-align:center;line-height:30px}

  .section-bar{position:absolute;top:293px;height:23px;font-family:"Roboto Condensed",Arial,sans-serif;font-weight:400;color:#fff;font-size:19px;line-height:23px}
  .section-bar b{font-weight:700}
  .section-bar--left{left:0;padding-left:30px;width:280px}
  .section-bar--right{left:610px;padding-left:37px;width:268px}

  .body-copy{position:absolute;font-size:9.8px;line-height:12.3px;color:#333;text-align:justify}
  .body-copy p{margin-bottom:12px}
  .body-copy--main{left:30px;top:328px;width:376px}
  .body-copy--side{left:658px;width:195px;border-left:1px solid #555;padding-left:9px;text-align:justify}
  .body-copy--side.one{top:352px}
  .body-copy--side.two{top:502px}
</style>
</head>
<body>

<!-- Outside: back cover + front cover -->
<section class="spread spread--cover">
  <svg class="art" viewBox="0 0 878 626" aria-hidden="true">
    <defs>
      <linearGradient id="backBg" x1="0" y1="0" x2="1" y2="1">
        <stop offset="0" stop-color="#f6f6f6"/><stop offset="1" stop-color="#dcdcdc"/>
      </linearGradient>
      <linearGradient id="blueBand" x1="0" y1="0" x2="1" y2="0">
        <stop offset="0" stop-color="#0a7fc0"/><stop offset="1" stop-color="#1c9bd6"/>
      </linearGradient>
      <linearGradient id="frontBg" x1="0" y1="0" x2="1" y2="0">
        <stop offset="0" stop-color="#e6e6e6"/><stop offset=".5" stop-color="#fff"/><stop offset="1" stop-color="#ececec"/>
      </linearGradient>
    </defs>
    <rect x="0" y="0" width="440" height="626" fill="url(#backBg)"/>
    <rect x="440" y="0" width="438" height="626" fill="url(#frontBg)"/>
  </svg>

  <div class="ph drone-photo" role="img" aria-label="Camera drone with gimbal lens, shown in flight on a white background"></div>

  <svg class="art" viewBox="0 0 878 626" aria-hidden="true">
    <path d="M0,378 Q200,340 440,458 L440,505 Q230,430 0,448 Z" fill="var(--charcoal)"/>
    <path d="M0,440 Q230,420 440,466 L440,626 L0,626 Z" fill="url(#blueBand)"/>
  </svg>

  <svg class="ph" role="img" aria-label="Glass office tower seen from below against a bright sky" viewBox="0 0 438 470" style="left:440px;top:0;width:438px;height:470px">
    <defs>
      <linearGradient id="tower" x1="0" y1="1" x2="1" y2="0">
        <stop offset="0" stop-color="#123f6b"/>
        <stop offset=".25" stop-color="#2c6fa8"/>
        <stop offset=".5" stop-color="#5b9fcf"/>
        <stop offset=".75" stop-color="#a9d5ec"/>
        <stop offset="1" stop-color="#f2f8fc"/>
      </linearGradient>
      <radialGradient id="skyGlow" cx=".78" cy=".22" r=".55">
        <stop offset="0" stop-color="#ffffff" stop-opacity=".85"/>
        <stop offset="1" stop-color="#ffffff" stop-opacity="0"/>
      </radialGradient>
    </defs>
    <path d="M0,0 H438 V366 Q210,380 0,466 Z" fill="url(#tower)"/>
    <path d="M0,0 H438 V366 Q210,380 0,466 Z" fill="url(#skyGlow)"/>
    <path d="M0,466 Q210,380 438,366 V412 Q240,410 0,470 Z" fill="var(--blue-main)"/>
  </svg>

  <div class="brand brand--front"><span class="brand__dot"></span><span>Highpoint Aerial<br>Imaging</span></div>

  <div class="contact">
    <h4>Contact Information:</h4>
    <ul>
      <li><svg viewBox="0 0 10 10"><path d="M2,1 L4,1 L4.6,3 L3.4,4 Q4.4,6 6,6.6 L7,5.4 L9,6 L9,8 Q5,9 1,4 Z" fill="#fff"/></svg>000-0000-000</li>
      <li><svg viewBox="0 0 10 10"><rect x="1" y="2" width="8" height="6" rx="1" fill="#fff"/></svg>000-0000-000</li>
      <li><svg viewBox="0 0 10 10"><path d="M1,2 H9 V8 H1 Z M1,2 L5,5.5 L9,2" fill="none" stroke="#fff" stroke-width="1.2"/></svg>hereyouremail.id</li>
      <li class="label">Address:</li>
      <li><svg viewBox="0 0 10 10"><path d="M5,0.5 A3.2,3.2 0 0 1 8.2,3.7 Q8.2,6 5,9.5 Q1.8,6 1.8,3.7 A3.2,3.2 0 0 1 5,0.5 Z" fill="#fff"/></svg>Lorem Ipsum is simply dummy<br>text of the printing</li>
      <li><svg viewBox="0 0 10 10"><circle cx="5" cy="5" r="4" fill="none" stroke="#fff" stroke-width="1.2"/><path d="M1,5 H9 M5,1 Q2.5,5 5,9 Q7.5,5 5,1" fill="none" stroke="#fff" stroke-width=".8"/></svg>company.website.com</li>
    </ul>
  </div>

  <div class="brand brand--back"><span class="brand__dot"></span><span>Highpoint Aerial<br>Imaging</span></div>

  <h1 class="cover-title"><span class="light">AERIAL</span><span class="bold">PHOTOGRAPHY</span></h1>
  <div class="web-pill">www.companywebsite.com</div>
  <div class="fold"></div>
</section>

<!-- Inside spread -->
<section class="spread spread--inside">
  <svg class="ph" role="img" aria-label="City skyline at sunset seen from above" viewBox="0 0 878 260" style="left:0;top:0;width:878px;height:260px">
    <defs>
      <linearGradient id="city" x1="0" y1="0" x2="0" y2="1">
        <stop offset="0" stop-color="#f2c97c"/><stop offset=".3" stop-color="#c99a63"/><stop offset=".6" stop-color="#6b6360"/><stop offset="1" stop-color="#2f3947"/>
      </linearGradient>
      <radialGradient id="sun" cx=".33" cy=".05" r=".35">
        <stop offset="0" stop-color="#fff6dc" stop-opacity=".95"/><stop offset="1" stop-color="#fff6dc" stop-opacity="0"/>
      </radialGradient>
    </defs>
    <path d="M130,0 H878 V170 Q820,244 700,250 Q560,252 440,196 Q300,80 130,0 Z" fill="url(#city)"/>
    <path d="M130,0 H878 V170 Q820,244 700,250 Q560,252 440,196 Q300,80 130,0 Z" fill="url(#sun)"/>
  </svg>

  <svg class="art" viewBox="0 0 878 626" aria-hidden="true">
    <path d="M0,0 H130 Q300,80 440,196 Q250,122 0,112 Z" fill="var(--charcoal)"/>
    <path d="M0,293 H255 L280,316 H405 V318 H0 Z" fill="var(--blue-main)"/>
    <path d="M470,316 H610 L635,293 H878 V318 H470 Z" fill="var(--blue-main)"/>
  </svg>

  <div class="brand brand--inside"><span class="brand__dot"></span><span>Highpoint Aerial<br>Imaging</span></div>

  <h2 class="section-bar section-bar--left">AERIAL <b>PHOTOGRAPHY</b></h2>
  <h2 class="section-bar section-bar--right">AERIAL <b>PHOTOGRAPHY</b></h2>

  <div class="body-copy body-copy--main">
    <p>We capture your project from above with licensed pilots and stable camera drones. Every flight is planned around your site, your schedule and the light, so the images arrive sharp, level and ready to share. Builders use our views to follow jobsite progress, while agents use them to show a property and its lot.</p>
    <p>Each visit ends with a clean set of edited stills and short video clips. Files are delivered online within two business days, sized for print, web pages and listings of any kind.</p>
    <p>Commercial clients book monthly flights to record a build from ground work to roof. The same angles are repeated each time, so change is easy to see and simple to report to owners.</p>
    <p>We carry full insurance and follow local airspace rules on every job. Before a flight we check the weather, the site and any nearby traffic, and we keep owners informed from booking to delivery so there are no surprises along the way.</p>
    <p>Visit our website to see recent work, compare packages and book your first flight with our team today.</p>
  </div>

  <div class="ph" role="img" aria-label="Drone flying over a city at sunrise" style="left:474px;top:343px;width:146px;height:114px;background:radial-gradient(ellipse at 30% 20%,#fff1c8 0%,rgba(255,241,200,0) 45%),linear-gradient(170deg,#f3c77a 0%,#d9934a 55%,#6e5240 100%)"></div>
  <div class="ph" role="img" aria-label="Overhead view of a waterfront office block and city streets" style="left:474px;top:481px;width:146px;height:115px;background:linear-gradient(160deg,#7f95ab 0%,#a9b3ba 45%,#5d7384 75%,#2f4b5e 100%)"></div>

  <div class="body-copy body-copy--side one"><p>Real estate packages include wide views of the home, the lot and the street, plus close passes over pools, gardens and rooftops. Images are colour corrected and ready for any listing site.</p></div>
  <div class="body-copy body-copy--side two"><p>Jobsite packages follow a fixed flight path on each visit. Owners, lenders and crews get a clear record of progress they can compare month by month.</p></div>

  <div class="fold"></div>
</section>

</body>
</html>
```